Information Prospectus for education sector

We need to create a 12 page information memorandum reagrding the education an industry snapshot in Australia, This will be sent to investors in Australia and overseas looking to invest into the education sector in Australia.

Target Market(s)

Investors into the education sector

Industry/Entity Type

Education

Font styles to use
Sans Serif

Colors
fbee3d
33a6d7
9bcb3c

```html
<!DOCTYPE html>
<html lang="en">
<head>
<meta charset="utf-8">
<title>Orvell Corp – International Education Industry Snapshot</title>
<link href="https://fonts.googleapis.com/css2?family=Nunito+Sans:wght@400;600;700;800&display=swap" rel="stylesheet">
<style>
  :root {
    --bg: #9a9a9a;
    --blue: #0f63c0;
    --sky: #33a6d7;
    --green: #9bcb3c;
    --green-deep: #6f9e1e;
    --navy: #2f3d9e;
    --navy-deep: #263182;
    --ink: #2a2a2a;
    --purple: #3b2a86;
    --map: #3d3596;
    --cream: #fbf3e6;
    --lilac: #e9e8f4;
    --white: #ffffff;
  }
  * { box-sizing: border-box; margin: 0; padding: 0; }
  html, body { width: 1200px; height: 1200px; overflow: hidden; }
  body {
    background: radial-gradient(circle at 50% 45%, #a7a7a7 0%, var(--bg) 70%, #8a8a8a 100%);
    font-family: "Nunito Sans", sans-serif;
    position: relative;
  }
  .page {
    position: absolute; width: 546px; height: 386px; background: var(--white);
    overflow: hidden; box-shadow: 0 2px 6px rgba(0,0,0,.25);
  }
  .cover { left: 38px; top: 200px; background: var(--blue); }
  .intro { left: 616px; top: 200px; }
  .industry { left: 327px; top: 614px; }

  /* cover */
  .cover svg { position: absolute; inset: 0; }
  .cover-title {
    position: absolute; left: 362px; top: 168px; color: var(--white);
    font-size: 14px; line-height: 17.6px; font-weight: 400; letter-spacing: .2px;
  }
  .cover-rule { position: absolute; left: 442px; top: 210px; width: 104px; height: 2px; background: var(--white); }
  .cover-brand {
    position: absolute; left: 0; top: 329px; width: 352px; height: 27px; background: var(--sky);
    color: var(--white); font-weight: 800; font-size: 16px; line-height: 27px; padding-left: 22px;
  }

  /* intro */
  .intro-photo {
    position: absolute; left: 0; top: 0; width: 84px; height: 386px;
    background: linear-gradient(160deg, #b9e065 0%, var(--green) 45%, var(--green-deep) 100%);
  }
  .intro-tag {
    position: absolute; left: 48px; top: 236px; width: 36px; height: 120px;
    background: var(--white);
  }
  .intro-tag::before {
    content: ""; position: absolute; left: 3px; top: 3px; right: 0; bottom: 3px;
    border: 1.5px solid var(--ink); border-right: none;
  }
  .intro-tag span {
    position: absolute; left: 50%; top: 50%; transform: translate(-50%,-50%) rotate(-90deg);
    white-space: nowrap; font-weight: 800; font-size: 14px; color: var(--ink);
  }
  .intro-copy {
    position: absolute; left: 136px; top: 64px; width: 366px; color: var(--ink);
    font-size: 11px; line-height: 14px;
  }
  .intro-copy p { margin-bottom: 14px; }
  .intro-copy .justified { text-align: justify; }

  /* industry */
  .industry-strip { position: absolute; left: 0; top: 0; width: 280px; height: 16px; background: var(--navy); }
  .industry-title {
    position: absolute; left: 0; top: 23px; width: 546px; text-align: center;
    font-size: 18px; font-weight: 400; color: var(--ink); letter-spacing: .1px;
  }
  .industry-panel {
    position: absolute; left: 0; top: 51px; width: 280px; height: 335px; background: var(--navy);
  }
  .skyline { position: absolute; left: 0; bottom: 0; width: 280px; height: 110px;
    background: linear-gradient(180deg, rgba(47,61,158,0) 0%, var(--navy-deep) 55%, #1e2870 100%); }
  .industry-copy {
    position: absolute; left: 20px; top: 26px; width: 240px; color: var(--white);
    font-size: 9.6px; line-height: 12.5px; text-align: justify;
  }
  .industry-copy h3 { font-size: 9.6px; font-weight: 800; margin: 12px 0 5px; }

  .facts { position: absolute; left: 294px; top: 74px; width: 238px; color: var(--purple); }
  .facts-map { position: relative; height: 116px; background: var(--cream); }
  .map-head { position: absolute; left: 13px; top: 14px; font-size: 7.2px; line-height: 8.8px; }
  .map-head b { font-weight: 800; }
  .map-area {
    position: absolute; left: 66px; top: 6px; width: 128px; height: 90px;
    background: var(--map); border-radius: 8px;
  }
  .state { position: absolute; text-align: center; font-size: 7px; line-height: 7px; font-weight: 800; color: var(--white); }
  .state small { display: block; font-size: 3.4px; line-height: 4px; font-weight: 600; }
  .state.outside { color: var(--purple); }
  .facts-badge {
    position: absolute; right: 4px; top: 8px; width: 54px; height: 54px; border-radius: 50%;
    border: 2px solid var(--purple); background: var(--white); text-align: center;
    font-size: 4.4px; line-height: 5.2px; padding-top: 10px;
  }
  .facts-badge b { display: block; font-size: 8px; line-height: 10px; font-weight: 800; }
  .fact-row {
    display: flex; align-items: center; height: 35px; background: var(--lilac);
    border-top: 1px dashed #9a96c8; font-size: 6.4px; line-height: 8px;
  }
  .fact-row .icon { flex: none; width: 56px; height: 20px; margin: 0 27px 0 19px; background: #4a3ea0; border-radius: 2px; }
  .fact-row span { width: 130px; }
  .fact-row b { font-weight: 800; }
  .facts-source { margin-top: 15px; font-size: 6.6px; color: var(--ink); text-align: center; }
</style>
</head>
<body>

<section class="page cover">
  <svg width="546" height="386" viewBox="0 0 546 386">
    <defs>
      <linearGradient id="towerTone" x1="0" y1="0" x2="0.4" y2="1">
        <stop offset="0" stop-color="#dfe9f2"/>
        <stop offset=".5" stop-color="#9fb6cb"/>
        <stop offset="1" stop-color="#5d7590"/>
      </linearGradient>
    </defs>
    <polygon points="0,0 278,0 360,386 0,386" fill="url(#towerTone)" role="img" aria-label="Photograph of a glass office tower against a bright sky"/>
    <polygon points="278,0 290,0 372,386 360,386" fill="var(--sky)"/>
  </svg>
  <div class="cover-title">THE INTERNATIONAL<br>EDUCATION INDUSTRY<br>SNAPSHOT</div>
  <div class="cover-rule"></div>
  <div class="cover-brand">ORVELL CORP</div>
</section>

<section class="page intro">
  <div class="intro-photo" role="img" aria-label="Photograph of a building facade tinted green"></div>
  <div class="intro-tag"><span>ORVELL CORP</span></div>
  <div class="intro-copy">
    <p>ORVELL CORP is an independent and Australian owned agency providing premium specialist services to investors, buyers and sellers across the private education markets.</p>
    <p>Our team consists of people with a long-term successful career in the education industry. The team is a knowledgeable and informed group of professionals with a strong commitment and attitude which allows us to professionally drive negotiations.</p>
    <p class="justified">In the first six months of 2018, we have successfully completed many transactions in the sale of international education institutes. We currently have investment and acquisition opportunities from $1m to $15m.</p>
    <p>Throughout this presentation, prospective investors will have an insight knowledge of:<br>The outlook and growth of International Education Industry in Australia<br>Investment opportunity of International Education Industry in Australia<br>Investment return and risks.</p>
  </div>
</section>

<section class="page industry">
  <div class="industry-strip"></div>
  <h2 class="industry-title">INTERNATIONAL EDUCATION INDUSTRY IN AUSTRALIA</h2>
  <div class="industry-panel">
    <div class="skyline" role="img" aria-label="Photograph of a city skyline tinted blue"></div>
    <div class="industry-copy">
      <p>In 2016-2017, the Education Industry generated $28.6 Billion to the Australian Economy and was the third largest source of export income for Australia after Iron and Coal. It increased 16.1% compared to 2015-2016 Financial Year which was $24.145 Billion. The growth in Education Export has been very sustainable with the average growth of 11% in the last 5 years.</p>
      <h3>BUSINESS OPPORTUNITIES</h3>
      <p>The higher education sector generated $19.1 billion in export income (68.1% of total on-shore earnings). The VET sector generated $4.8 billion in earnings (17.3% of total), ELICOS was $1.4 billion (5.2%); schools was $1.2 billion (4.4%); and non-award was $981 million (3.5%).</p>
    </div>
  </div>
  <div class="facts">
    <div class="facts-map">
      <div class="map-head"><b>2016–17<br>export income</b><br>by state and<br>territory</div>
      <div class="map-area" role="img" aria-label="Map of Australia divided into states and territories"></div>
      <div class="state" style="left:80px;top:50px">WA<small>$3,886<br>MILLION</small></div>
      <div class="state" style="left:116px;top:32px">NT<small>$88<br>MILLION</small></div>
      <div class="state" style="left:150px;top:37px">QLD<small>$4,516<br>MILLION</small></div>
      <div class="state" style="left:116px;top:58px">SA<small>$1,468 MILLION</small></div>
      <div class="state" style="left:154px;top:65px">NSW<small>$10,394<br>MILLION</small></div>
      <div class="state outside" style="left:200px;top:82px">ACT<small>$796<br>MILLION</small></div>
      <div class="state outside" style="left:124px;top:97px">VIC<small>$8,005 MILLION</small></div>
      <div class="state outside" style="left:174px;top:99px">TAS<small>$239 MILLION</small></div>
      <div class="facts-badge">International<br>education is worth<b>28.6 billion</b>to the Australian<br>economy</div>
    </div>
    <div class="fact-row"><div class="icon" role="img" aria-label="Illustration of an education crate with a third place ribbon"></div><span>Education is the <b>3rd largest<br>export</b> for Australia</span></div>
    <div class="fact-row"><div class="icon" role="img" aria-label="Illustration of a group of workers"></div><span>International education supports<br><b>130,000 jobs</b> nationally</span></div>
    <div class="fact-row"><div class="icon" role="img" aria-label="Illustration of landmark buildings"></div><span><b>China 28% and India 11%</b> are the<br><b>largest sources</b> of international<br>students in 2016</span></div>
    <div class="fact-row"><div class="icon" role="img" aria-label="Illustration of a graduation cap and tools"></div><span><b>43%</b> of international enrolments in 2016<br>are in <b>higher education</b> and <b>26%</b> in<br><b>vocational education and training</b></span></div>
    <p class="facts-source">Sourced from The National Education Statistics Office</p>
  </div>
</section>

</body>
</html>
```